Business Card Design for a Lending Business (Hard Money loans)

We need a business card for our Real Estate Lending business. We do hard Money loans for real estate investors. We have an existing logo we like, see attached. I'd like the business card to mostly include the logo colors, but a bright color pop of some sort would be nice to see also. Card should include Logo, Company Name, Company Address, Employee Name, Cell Phone, Main Phone, Email, Website

Industry/Entity Type

Finance / Lending

Contact Information for Business Card

Logo, Company Name, Company Address, Employee Name, Cell Phone, Main Phone, Email, Website

Requirements
Nice to have
• I'd like the business card to mostly include the logo colors, but a bright color pop of some sort would be nice to see also.

```html
<!DOCTYPE html>
<html lang="en">
<head>
<meta charset="utf-8">
<title>Harborline Lending – Business Card</title>
<link rel="stylesheet" href="https://fonts.googleapis.com/css2?family=Montserrat:wght@700;800&family=Lato:wght@400;700&display=swap">
<style>
  :root {
    --navy: #27337f;
    --cyan: #0fa9dc;
    --ink-grey: #5a5f6b;
    --card: #ffffff;
    --backdrop: #2b2d31;
  }
  * { box-sizing: border-box; margin: 0; padding: 0; }
  html, body { width: 1200px; height: 952px; overflow: hidden; }
  body {
    background: var(--backdrop);
    position: relative;
    font-family: "Lato", sans-serif;
  }
  .card {
    position: absolute;
    width: 540px;
    height: 310px;
    background: var(--card);
    border-radius: 22px;
    overflow: hidden;
    box-shadow: 0 14px 34px rgba(0,0,0,0.45);
  }
  .card--front { left: 60px; top: 120px; }
  .card--back  { left: 600px; top: 520px; }

  /* Front */
  .wordmark {
    position: absolute;
    inset: 0;
    display: flex;
    align-items: center;
    justify-content: center;
    gap: 14px;
  }
  .wordmark__dot {
    width: 26px; height: 26px;
    border-radius: 50%;
    background: var(--cyan);
  }
  .wordmark__name {
    font-family: "Montserrat", sans-serif;
    font-weight: 800;
    font-size: 30px;
    letter-spacing: 2px;
    color: var(--navy);
  }

  /* Back */
  .back__accent {
    position: absolute;
    left: -70px; top: 10px;
    width: 290px; height: 290px;
    border-radius: 50%;
    background: var(--navy);
  }
  .details {
    position: absolute;
    right: 34px; top: 38px;
    text-align: right;
  }
  .person__name {
    font-family: "Montserrat", sans-serif;
    font-weight: 700;
    font-size: 20px;
    color: var(--navy);
    letter-spacing: 0.5px;
  }
  .person__name .surname { color: var(--cyan); font-weight: 800; }
  .person__title {
    font-size: 13px;
    color: var(--ink-grey);
    margin-top: 2px;
  }
  .contacts { list-style: none; margin-top: 16px; }
  .contacts li {
    display: flex;
    align-items: center;
    justify-content: flex-end;
    gap: 8px;
    font-size: 12.5px;
    color: var(--ink-grey);
    margin-bottom: 5px;
  }
  .contacts .icon {
    width: 17px; height: 17px;
    border-radius: 3px;
    background: var(--cyan);
    display: flex; align-items: center; justify-content: center;
  }
  .company { margin-top: 18px; }
  .company__name {
    font-family: "Montserrat", sans-serif;
    font-weight: 800;
    font-size: 15px;
    color: var(--navy);
    letter-spacing: 0.5px;
  }
  .company__address {
    font-size: 12.5px;
    color: var(--ink-grey);
    line-height: 1.35;
    margin-top: 3px;
  }
</style>
</head>
<body>

  <section class="card card--front" aria-label="Card front">
    <div class="wordmark">
      <span class="wordmark__dot"></span>
      <span class="wordmark__name">HARBORLINE LENDING</span>
    </div>
  </section>

  <section class="card card--back" aria-label="Card back">
    <div class="back__accent"></div>
    <div class="details">
      <p class="person__name">DANIEL R. <span class="surname">WHITFORD</span></p>
      <p class="person__title">Managing Director</p>

      <ul class="contacts">
        <li>+00 123 456 78
          <span class="icon">
            <svg width="11" height="11" viewBox="0 0 24 24"><path fill="#fff" d="M6.6 10.8a15 15 0 0 0 6.6 6.6l2.2-2.2a1 1 0 0 1 1-.25 11.4 11.4 0 0 0 3.6.57 1 1 0 0 1 1 1V20a1 1 0 0 1-1 1A17 17 0 0 1 3 4a1 1 0 0 1 1-1h3.5a1 1 0 0 1 1 1c0 1.25.2 2.45.57 3.57a1 1 0 0 1-.25 1z"/></svg>
          </span>
        </li>
        <li>hello@harborlinelending.com
          <span class="icon">
            <svg width="11" height="11" viewBox="0 0 24 24"><rect x="2" y="5" width="20" height="14" rx="1.5" fill="none" stroke="#fff" stroke-width="2"/><path d="M3 6l9 7 9-7" fill="none" stroke="#fff" stroke-width="2"/></svg>
          </span>
        </li>
        <li>www.harborlinelending.com
          <span class="icon">
            <svg width="11" height="11" viewBox="0 0 24 24"><path fill="#fff" d="M12 2a7 7 0 0 0-7 7c0 5.25 7 13 7 13s7-7.75 7-13a7 7 0 0 0-7-7zm0 9.5A2.5 2.5 0 1 1 12 6.5a2.5 2.5 0 0 1 0 5z"/></svg>
          </span>
        </li>
      </ul>

      <div class="company">
        <p class="company__name">HARBORLINE LENDING LTD</p>
        <p class="company__address">1720 Ridgecrest Avenue<br>Arlington, VA 22201</p>
      </div>
    </div>
  </section>

</body>
</html>
```